Brochure for staffing agency

I need a tri-fold brochure for our staffing agency. I also need a pdf ad to use that matches the brochure. It needs to be 4” wide x 5.5” tall and full color. Please look at our website www.brightquarrystaffing.com.

```html
<!DOCTYPE html>
<html lang="en">
<head>
<meta charset="utf-8">
<title>Bright Quarry Staffing – Tri-fold Brochure</title>
<link href="https://fonts.googleapis.com/css2?family=Prata&family=Montserrat:wght@400;500;600;700&display=swap" rel="stylesheet">
<style>
:root{
  --green:#3ba546;
  --green-dark:#2f8f3a;
  --purple:#5a2d91;
  --ink:#2b2b2b;
  --paper:#f7f7f7;
  --paper-grey:#ecedee;
  --stage:#e9eaeb;
  --serif:"Prata", Georgia, serif;
  --sans:"Montserrat", Arial, sans-serif;
}
*{box-sizing:border-box;margin:0;padding:0}
html,body{width:1200px;height:2393px;overflow:hidden}
body{background:var(--stage);font-family:var(--sans);color:var(--ink);position:relative}

.cover-single{position:absolute;left:470px;top:40px;width:347px;height:803px;transform:scale(.747);transform-origin:0 0;box-shadow:0 6px 18px rgba(0,0,0,.12)}
.spread{position:absolute;left:80px;width:1040px;height:803px;display:flex;box-shadow:0 6px 18px rgba(0,0,0,.12)}
.spread--outside{top:688px}
.spread--inside{top:1536px}
.panel{position:relative;width:346.67px;height:803px;overflow:hidden;background:var(--paper)}
.spread--inside .panel{background:linear-gradient(180deg,#e4e5e6 0%,var(--paper-grey) 35%,#f4f4f4 100%)}

/* cover */
.cover__green{position:absolute;left:0;top:0;width:100%;height:370px;background:linear-gradient(180deg,var(--green) 0%,var(--green) 70%,var(--green-dark) 100%)}
.brand{position:absolute;display:flex;align-items:center;gap:8px;color:#fff}
.brand__dot{width:14px;height:14px;border-radius:50%;background:currentColor;flex:none}
.brand__name{font-family:var(--sans);font-weight:500;font-size:22px;line-height:1}
.brand__tag{position:absolute;font-size:10px;font-weight:500;color:#fff}
.cover .brand{left:40px;top:70px}
.cover .brand__tag{left:150px;top:98px}
.photo{position:absolute}
.cover__photo{left:42px;top:170px;width:305px;height:335px;background:linear-gradient(135deg,#f3f5f7 0%,#dfe6ec 45%,#c9b6a0 70%,#e8ecef 100%)}
.cover__headline{position:absolute;left:20px;right:20px;top:538px;text-align:center;font-family:var(--serif);color:var(--purple);font-size:37px;line-height:1.02;letter-spacing:.5px}
.cover__lede{position:absolute;left:30px;right:30px;top:630px;text-align:center;font-weight:600;font-size:16px;line-height:1.3;color:#222}
.pill{position:absolute;left:26px;right:26px;top:722px;height:36px;border-radius:18px;background:var(--purple);color:#fff;font-weight:500;font-size:13px;display:flex;align-items:center;justify-content:center}

/* about */
.panel-title{font-family:var(--serif);color:var(--purple);text-transform:uppercase;line-height:1.1}
.about__title{position:absolute;left:40px;top:40px;font-size:24px}
.about__body{position:absolute;left:40px;right:30px;top:120px;font-size:10.5px;line-height:1.45;color:#333}
.about__body p+p{margin-top:10px}
.about__photo{left:0;bottom:0;width:100%;height:250px;background:linear-gradient(180deg,#eef1f3 0%,#dde3e6 40%,#c7ccce 60%,var(--green) 61%,var(--green-dark) 100%)}

/* testimonials & contact */
.quotes{position:absolute;left:0;top:0;width:100%;height:400px}
.quote-mark{position:absolute;font-family:var(--serif);color:var(--purple);font-size:96px;line-height:1}
.quote-mark--open{left:30px;top:20px}
.quote-mark--close{right:30px;top:300px}
.quote-rule{position:absolute;left:110px;right:40px;top:70px;border-top:1.5px solid #fff}
.quote-rule--bottom{left:40px;right:110px;top:350px}
.quotes__text{position:absolute;left:40px;right:40px;top:88px;color:#fff;font-size:11px;line-height:1.4}
.quotes__who{font-weight:700;font-size:10px;text-transform:uppercase;margin:6px 0 12px}
.contact .brand{color:var(--green);left:78px;top:440px}
.contact .brand__name{font-size:19px}
.contact__tag{position:absolute;left:180px;top:462px;font-size:9px;color:var(--green);font-weight:500}
.contact__offices{position:absolute;left:20px;right:20px;top:500px;text-align:center;font-size:12px;line-height:1.35;color:#333}
.contact__offices p+p{margin-top:12px}
.contact__person{position:absolute;left:20px;right:20px;top:762px;text-align:center;font-size:11.5px;font-weight:600;color:var(--purple)}

/* services */
.service{position:absolute;left:34px;right:30px}
.icon-circle{width:30px;height:30px;border:1.5px dashed var(--green);border-radius:50%;display:flex;align-items:center;justify-content:center;color:var(--green);margin-bottom:8px}
.service__label{display:inline-block;background:var(--green);color:#fff;font-family:var(--serif);font-size:16px;padding:3px 10px;margin-bottom:8px}
.service__text{font-size:10.5px;line-height:1.4;color:#333}

/* industries */
.industries__title{position:absolute;left:0;right:0;top:44px;text-align:center;font-size:20px}
.industry{position:absolute;left:30px;right:30px;height:60px;display:flex;align-items:center;gap:14px}
.industry--right{flex-direction:row-reverse}
.industry__icon{width:58px;height:58px;flex:none;border:2px dashed var(--green);border-radius:50%;display:flex;align-items:center;justify-content:center;color:var(--green)}
.industry__name{font-family:var(--serif);font-size:14px;line-height:1.15;color:#444;flex:1;text-align:center}

/* hire */
.hire__title{position:absolute;left:36px;right:30px;top:44px;font-size:21px}
.hire__text{position:absolute;left:36px;right:30px;top:140px;font-size:10.5px;line-height:1.45;color:#333}
.hire__band{position:absolute;left:0;top:280px;width:100%;height:150px;background:var(--green)}
.hire__phones{position:absolute;left:36px;top:305px;color:#fff;font-size:16px;font-weight:500;line-height:1.55}
.hire__photo-back{position:absolute;left:0;top:420px;width:100px;height:383px;background:linear-gradient(180deg,var(--green) 0%,var(--green-dark) 100%)}
.hire__photo{left:90px;top:420px;width:257px;height:383px;background:linear-gradient(150deg,#f1f1ee 0%,#d8d4cc 45%,#3a3a42 65%,#e3b26a 100%)}
</style>
</head>
<body>

<!-- front cover on its own -->
<section class="panel cover cover-single">
  <div class="cover__green"></div>
  <div class="brand"><span class="brand__dot"></span><span class="brand__name">bright quarry staffing</span></div>
  <span class="brand__tag">recruiting + staffing</span>
  <div class="photo cover__photo" role="img" aria-label="Photo of a smiling businesswoman holding a tablet in a bright office"></div>
  <h1 class="cover__headline">VISION.ACTION.<br>RESULTS.</h1>
  <p class="cover__lede">We are a team of dedicated professionals who are committed to the success of our customer.</p>
  <div class="pill">www.brightquarrystaffing.com</div>
</section>

<!-- outside spread -->
<section class="spread spread--outside">
  <article class="panel about">
    <h2 class="panel-title about__title">About Bright<br>Quarry Staffing</h2>
    <div class="about__body">
      <p>Bright Quarry Staffing is a staffing and recruitment company working for companies and individuals based across the United States.</p>
      <p>In May of 1998, Bright Quarry Staffing was purchased by Carver Holdings, LLC, which is owned by Helen and Paul Carver. Their vision was to take the 1967-founded company to a new capacity level by branching out and providing new niche services to government and commercial customers throughout the southeast.</p>
      <p>In 2018 the company located their principal business at 84 Market Street on the historic square in Linton. They continue to have a satellite facility at 300 Route 9, Suite C in Maple Ridge.</p>
      <p>President Helen Carver was selected as one of the Top 40 Under 40 in the state. She has served on the highly visible regional Board of Directors, the Governor's Council on Junior Colleges, and many religious and philanthropic organizations throughout the state.</p>
    </div>
    <div class="photo about__photo" role="img" aria-label="Photo of a businessman working at a high table by a window"></div>
  </article>

  <article class="panel contact">
    <svg class="quotes" viewBox="0 0 347 400" preserveAspectRatio="none" aria-hidden="true">
      <path d="M0 0H347V330Q180 390 0 400Z" fill="var(--green)"/>
    </svg>
    <span class="quote-mark quote-mark--open">&#8220;</span>
    <span class="quote-rule"></span>
    <div class="quotes__text">
      <p>I spent months trying to find a job on my own and didn't get anywhere. Don't waste your time and reach out to Bright Quarry Staffing as soon as possible.</p>
      <p class="quotes__who">Jordan, Bright Quarry Staffing job seeker</p>
      <p>I am grateful for the opportunity to work this contract position the last 2 years. Never before have I seen an owner roll up their sleeves and get their hands dirty with the employees as much as I did Helen. Also, thank you to Sam for his advice, wisdom, and leadership that made me a better employee.</p>
      <p class="quotes__who">Riley, Bright Quarry Staffing temp employee</p>
    </div>
    <span class="quote-rule quote-rule--bottom"></span>
    <span class="quote-mark quote-mark--close">&#8221;</span>
    <div class="brand"><span class="brand__dot"></span><span class="brand__name">bright quarry staffing</span></div>
    <span class="contact__tag">recruiting + staffing</span>
    <div class="contact__offices">
      <p>Linton Headquarters<br>84 Market Street<br>Linton, MS 39000 (directions)<br>(555) 010-4161</p>
      <p>Maple Ridge Branch<br>300 Route 9, Suite C<br>Maple Ridge, MS 39100 (directions)<br>(555) 010-8985</p>
      <p>Easton Branch<br>22 Elm Street<br>Easton, MS 39200<br>(555) 010-2427</p>
      <p>Fairview Branch<br>(555) 010-5739</p>
    </div>
    <p class="contact__person">Morgan Lane, mlane@brightquarrystaffing.com</p>
  </article>

  <article class="panel cover">
    <div class="cover__green"></div>
    <div class="brand"><span class="brand__dot"></span><span class="brand__name">bright quarry staffing</span></div>
    <span class="brand__tag">recruiting + staffing</span>
    <div class="photo cover__photo" role="img" aria-label="Photo of a smiling businesswoman holding a tablet in a bright office"></div>
    <h1 class="cover__headline">VISION.ACTION.<br>RESULTS.</h1>
    <p class="cover__lede">We are a team of dedicated professionals who are committed to the success of our customer.</p>
    <div class="pill">www.brightquarrystaffing.com</div>
  </article>
</section>

<!-- inside spread -->
<section class="spread spread--inside">
  <article class="panel services">
    <div class="service" style="top:40px">
      <div class="icon-circle"><svg width="14" height="14" viewBox="0 0 14 14"><circle cx="7" cy="7" r="5.5" fill="none" stroke="currentColor" stroke-width="1.4"/><path d="M7 3.5V7l2.5 1.5" fill="none" stroke="currentColor" stroke-width="1.4"/></svg></div>
      <div class="service__label">Temp &amp; Contract Staffing</div>
      <p class="service__text">If you have a short-term assignment or temporary role to fill, Bright Quarry Staffing offers temporary and contract position staffing and recruitment services for a wide variety of clients and industries.</p>
    </div>
    <div class="service" style="top:220px">
      <div class="icon-circle"><svg width="14" height="14" viewBox="0 0 14 14"><circle cx="7" cy="5" r="2.6" fill="currentColor"/><path d="M2 13q5-7 10 0z" fill="currentColor"/></svg></div>
      <div class="service__label">Direct Placement</div>
      <p class="service__text">Fill your permanent roles with qualified candidates throughout direct placement services. We are trusted by some of the nation's top companies to headhunt top talent for their organizations.</p>
    </div>
    <div class="service" style="top:400px">
      <div class="icon-circle"><svg width="14" height="14" viewBox="0 0 14 14"><circle cx="7" cy="5" r="2.6" fill="currentColor"/><path d="M2 13q5-7 10 0z" fill="currentColor"/></svg></div>
      <div class="service__label">Executive Search</div>
      <p class="service__text">Find the next leader of your organization. Do you need highly qualified candidates for senior-level and executive jobs in your organization? Our firm is highly experienced in headhunting for public, private, and non-profit sector executive positions.</p>
    </div>
    <div class="service" style="top:590px">
      <div class="icon-circle"><svg width="14" height="14" viewBox="0 0 14 14"><circle cx="7" cy="7" r="5" fill="none" stroke="currentColor" stroke-width="1.4"/><path d="M4.5 7.2l1.8 1.8 3.4-3.6" fill="none" stroke="currentColor" stroke-width="1.4"/></svg></div>
      <div class="service__label">Other Services</div>
      <p class="service__text">Bright Quarry Staffing offers additional services to employers including subject matter expert consultation, mystery shopping, outplacement services, and salary surveys. We also offer referral rewards for recommended candidates who receive placement.</p>
    </div>
  </article>

  <article class="panel industries">
    <h2 class="panel-title industries__title">Industries</h2>
    <div class="industry" style="top:100px"><span class="industry__icon"><svg width="26" height="26" viewBox="0 0 26 26"><rect x="4" y="6" width="18" height="14" rx="2" fill="none" stroke="currentColor" stroke-width="2"/><path d="M8 16v-3M13 16v-6M18 16v-4" stroke="currentColor" stroke-width="2"/></svg></span><span class="industry__name">Accounting &amp;<br>Finance</span></div>
    <div class="industry industry--right" style="top:180px"><span class="industry__icon"><svg width="26" height="26" viewBox="0 0 26 26"><path d="M10 4h6v6h6v6h-6v6h-6v-6H4v-6h6z" fill="currentColor"/></svg></span><span class="industry__name">Medical<br>&amp; Healthcare</span></div>
    <div class="industry" style="top:260px"><span class="industry__icon"><svg width="26" height="26" viewBox="0 0 26 26"><path d="M6 9a6 6 0 0 1 12 0v5h-3V9M19 14h2v3h-2z" fill="none" stroke="currentColor" stroke-width="2"/><rect x="4" y="13" width="3" height="5" fill="currentColor"/></svg></span><span class="industry__name">Call Center &amp;<br>Customer Service</span></div>
    <div class="industry industry--right" style="top:340px"><span class="industry__icon"><svg width="26" height="26" viewBox="0 0 26 26"><path d="M3 10L13 4l10 6z M5 11h16M7 12v8M11 12v8M15 12v8M19 12v8M4 21h18" fill="none" stroke="currentColor" stroke-width="2"/></svg></span><span class="industry__name">Government<br>Services</span></div>
    <div class="industry" style="top:420px"><span class="industry__icon"><svg width="26" height="26" viewBox="0 0 26 26"><circle cx="13" cy="9" r="4" fill="currentColor"/><path d="M5 22q8-11 16 0z" fill="currentColor"/></svg></span><span class="industry__name">Human<br>Resources</span></div>
    <div class="industry industry--right" style="top:500px"><span class="industry__icon"><svg width="26" height="26" viewBox="0 0 26 26"><circle cx="11" cy="8" r="4" fill="currentColor"/><path d="M3 22q8-11 14 0z" fill="currentColor"/><circle cx="20" cy="17" r="3" fill="none" stroke="currentColor" stroke-width="2"/></svg></span><span class="industry__name">Office, Clerical<br>&amp; Administrative</span></div>
    <div class="industry" style="top:580px"><span class="industry__icon"><svg width="26" height="26" viewBox="0 0 26 26"><path d="M3 22V12l6 4v-4l6 4V6h4v16z" fill="currentColor"/></svg></span><span class="industry__name">Industrial &amp;<br>Manufacturing</span></div>
    <div class="industry industry--right" style="top:660px"><span class="industry__icon"><svg width="26" height="26" viewBox="0 0 26 26"><rect x="4" y="5" width="18" height="12" rx="1" fill="none" stroke="currentColor" stroke-width="2"/><path d="M9 21h8M13 17v4" stroke="currentColor" stroke-width="2"/></svg></span><span class="industry__name">Information<br>Technology</span></div>
  </article>

  <article class="panel hire">
    <h2 class="panel-title hire__title">Hire our experts to solve your staffing challenges</h2>
    <p class="hire__text">Our clients have access to on-demand talent when and where they need it. We partner with your business to understand your needs and deliver real results. If you're looking for a staffing company that is competent in your domain who can strategically partner with you, please contact us at one of our offices below.</p>
    <div class="hire__band"></div>
    <p class="hire__phones">Linton: (555) 010-4161<br>Maple Ridge: (555) 010-8985<br>Fairview: (555) 010-8325</p>
    <div class="hire__photo-back"></div>
    <div class="photo hire__photo" role="img" aria-label="Photo of a smiling woman at work in an office"></div>
  </article>
</section>

</body>
</html>
```